Business card design needed

We need something on the back that allows the customer to get five stamps then the sixth visit they get 25 dollars to spend.
Industry/Entity Type
Business
Contact Information for Business Card
Quality meat,value for money,spit roast hire, wholesale pubs clubs,cater for bbqs.marlow lane butchery 217 marlow lane.64739204.

```html
<!DOCTYPE html>
<html lang="en">
<head>
<meta charset="utf-8">
<title>Marlow Lane Butchery – Loyalty Card Back</title>
<link rel="stylesheet" href="https://fonts.googleapis.com/css2?family=Playfair+Display:wght@700;900&display=swap">
<style>
  :root {
    --ink-deep: #07090a;
    --ink-mid: #1c2325;
    --ink-soft: #2c3538;
    --mist: #86a3a5;
    --mist-dark: #4d6567;
    --cleaver: rgba(255,255,255,0.05);
    --text-light: #f4f4f2;
    --text-icon: #c3cccc;
    --offer-red: #e01b1b;
  }
  * { margin: 0; padding: 0; box-sizing: border-box; }
  html, body { width: 1200px; height: 741px; overflow: hidden; background: var(--ink-deep); }
  .card {
    position: relative;
    width: 1200px;
    height: 741px;
    overflow: hidden;
    font-family: "Playfair Display", "Times New Roman", serif;
    font-weight: 700;
    color: var(--text-light);
  }
  .card-backdrop { position: absolute; inset: 0; }
  .offer {
    position: absolute;
    left: 0;
    width: 1210px;
    text-align: center;
    letter-spacing: 2px;
    text-shadow: 0 3px 4px rgba(0,0,0,0.9);
  }
  .offer-line { font-size: 25px; line-height: 1; white-space: nowrap; }
  .offer-line--first { position: absolute; top: 238px; width: 100%; }
  .offer-line--second { position: absolute; top: 314px; width: 100%; padding-left: 14px; }
  .offer-amount {
    font-size: 64px;
    font-weight: 900;
    color: var(--offer-red);
    letter-spacing: 0;
    vertical-align: -4px;
  }
  .contact {
    position: absolute;
    right: 142px;
    top: 518px;
    list-style: none;
    text-align: right;
    font-size: 25px;
    letter-spacing: 2.4px;
    text-shadow: 0 2px 3px rgba(0,0,0,0.9);
  }
  .contact-item { height: 44.5px; display: flex; justify-content: flex-end; align-items: center; gap: 30px; }
  .contact-icon { width: 34px; height: 30px; flex: none; }
  .contact-icon path, .contact-icon rect, .contact-icon circle { fill: var(--text-icon); }
</style>
</head>
<body>
<main class="card">
  <svg class="card-backdrop" width="1200" height="741" viewBox="0 0 1200 741">
    <defs>
      <linearGradient id="mistFade" x1="0" y1="0" x2="0" y2="1">
        <stop offset="0" stop-color="var(--ink-deep)"/>
        <stop offset="0.55" stop-color="var(--ink-mid)"/>
        <stop offset="0.8" stop-color="var(--mist-dark)"/>
        <stop offset="1" stop-color="var(--mist)"/>
      </linearGradient>
      <linearGradient id="panelFade" x1="0" y1="0" x2="0" y2="1">
        <stop offset="0" stop-color="#0a0d0e"/>
        <stop offset="0.5" stop-color="#1d2427"/>
        <stop offset="1" stop-color="var(--ink-soft)"/>
      </linearGradient>
      <mask id="panelCut">
        <rect width="1200" height="741" fill="#fff"/>
        <circle cx="0" cy="0" r="185" fill="#000"/>
        <circle cx="1200" cy="0" r="185" fill="#000"/>
        <circle cx="0" cy="741" r="160" fill="#000"/>
        <circle cx="1200" cy="741" r="160" fill="#000"/>
      </mask>
    </defs>
    <rect class="backdrop-base" width="1200" height="741" fill="url(#mistFade)"/>
    <rect class="backdrop-panel" x="16" y="0" width="1168" height="724" fill="url(#panelFade)" mask="url(#panelCut)"/>
    <rect class="backdrop-panel-edge" x="996" y="455" width="2" height="269" fill="rgba(0,0,0,0.35)"/>
    <g role="img" aria-label="Faint crossed butcher's cleavers decoration">
      <rect x="270" y="130" width="250" height="360" rx="30" fill="var(--cleaver)" transform="rotate(-32 395 310)"/>
      <rect x="700" y="100" width="250" height="360" rx="30" fill="var(--cleaver)" transform="rotate(32 825 280)"/>
    </g>
  </svg>

  <section class="offer" aria-label="Loyalty offer">
    <p class="offer-line offer-line--first">spend <span class="offer-amount">$50</span> or more to recieve a stamp and recieve</p>
    <p class="offer-line offer-line--second"><span class="offer-amount">$25</span> off your 6th visit</p>
  </section>

  <ul class="contact">
    <li class="contact-item"><span>0264739204</span>
      <svg class="contact-icon" viewBox="0 0 34 30" aria-label="phone"><path d="M2 12c0-5 6-7 15-7s15 2 15 7v2h-8v-3H10v3H2z"/><rect x="6" y="15" width="22" height="11" rx="2"/></svg></li>
    <li class="contact-item"><span>217 marlow lane</span>
      <svg class="contact-icon" viewBox="0 0 34 30" aria-label="address"><circle cx="18" cy="3.5" r="3.2"/><path d="M15 8h5l4 8-2 1-3-5-1 6 4 11h-3l-3-9-3 9h-3l4-12 1-5-3 3-1 5h-2l1-6z"/></svg></li>
    <li class="contact-item"><span>marlowlnbutchery@mailbay.com</span>
      <svg class="contact-icon" viewBox="0 0 34 30" aria-label="email"><path d="M2 8h30v2L17 19 2 10z"/><path d="M2 12l15 9 15-9v11H2z"/></svg></li>
  </ul>
</main>
</body>
</html>
```